School Communication Email Template

Looking for a designer to create a couple simple email templates that are matching our brand colors and feel. Attached is the default email template that is currently being sent out. Company details can be shared upon request.

Template is to be used within the booking tool we use (snapshot below) and gmail. Template code is in HTML (see screenshot below).
Updates

Template code for website should be in HTML. Sorry if that created confusion.

Target Market(s)

Parents of kids enrolled in our classes

Industry/Entity Type

Kids sport classes

Font styles to use
Serif

Colors
0054AA
0677BA
7BADD7
CADEEF
E8F1F8
FFF300
FFF600
FEFA6F
FFFEC7
FFFEE8

Requirements
Must have
• Consistency with company brand/colors
Nice to have
• Flexibility to be adjusted as needed

```html
<!DOCTYPE html>
<html lang="en">
<head>
<meta charset="utf-8">
<title>Booking Details – Brightfield Kids</title>
<link href="https://fonts.googleapis.com/css2?family=Arimo:wght@400;700&display=swap" rel="stylesheet">
<style>
  :root {
    --page-bg: #e3e3e3;
    --card-bg: #fcf9f9;
    --row-bg: #e3e3e3;
    --ink: #222222;
    --ink-soft: #3f3f3f;
    --brand-blue: #0054aa;
    --brand-mid: #0677ba;
    --brand-yellow: #fff300;
    --brand-gold: #f6b928;
    --icon-blue: #1e5bb0;
  }
  * { box-sizing: border-box; margin: 0; padding: 0; }
  html, body { width: 707px; height: 1200px; overflow: hidden; }
  body {
    background: var(--page-bg);
    font-family: "Arimo", Arial, sans-serif;
    color: var(--ink);
    position: relative;
  }
  .brand {
    position: absolute; top: 58px; left: 0; width: 707px;
    display: flex; align-items: center; justify-content: center; gap: 12px;
  }
  .brand-dot { width: 44px; height: 44px; border-radius: 50%; background: var(--brand-gold); }
  .brand-name { font-size: 30px; font-weight: 700; color: var(--brand-blue); }
  .greeting {
    position: absolute; top: 163px; width: 100%; text-align: center;
    font-size: 34px; font-weight: 400;
  }
  .greeting strong { font-weight: 700; }
  .subtitle {
    position: absolute; top: 215px; width: 100%; text-align: center;
    font-size: 25px; color: var(--ink);
  }
  .card {
    position: absolute; left: 54px; top: 276px; width: 597px; height: 692px;
    background: var(--card-bg); border-radius: 26px; overflow: hidden;
    box-shadow: 0 4px 14px rgba(0,0,0,0.12);
  }
  .card-band {
    height: 22px;
    background: linear-gradient(90deg, var(--brand-yellow) 0%, #a7c23f 35%, #6c9e78 60%, var(--brand-mid) 82%, var(--brand-blue) 100%);
  }
  .details { list-style: none; }
  .detail {
    position: absolute; left: 43px; width: 513px; height: 68px;
    background: var(--row-bg); border-radius: 9px;
    display: flex; align-items: center; padding: 0 24px 0 14px;
    font-size: 19px;
  }
  .detail svg { width: 28px; height: 28px; flex: none; }
  .detail-label { margin-left: 47px; color: var(--ink-soft); }
  .detail-value { margin-left: auto; font-weight: 700; }
  .social {
    position: absolute; top: 1016px; left: 0; width: 707px;
    display: flex; justify-content: center; gap: 17px;
  }
  .social-link { width: 43px; height: 43px; border-radius: 50%; background: var(--brand-blue); }
  .social-link.alt { background: #4fa8e6; }
  .social-link.deep { background: #0a66c2; }
  .footer-note {
    position: absolute; top: 1087px; width: 100%; text-align: center;
    font-size: 15px; line-height: 26px; color: var(--ink-soft);
  }
  .copyright {
    position: absolute; top: 1145px; width: 100%; text-align: center;
    font-size: 15px; color: var(--ink-soft);
  }
</style>
</head>
<body>
  <header>
    <div class="brand">
      <span class="brand-dot"></span>
      <span class="brand-name">Brightfield Kids</span>
    </div>
    <h1 class="greeting">Hi <strong>Leo Marsh,</strong></h1>
    <p class="subtitle">your online booking details</p>
  </header>

  <main class="card">
    <div class="card-band"></div>
    <ul class="details">
      <li class="detail" style="top:74px">
        <svg viewBox="0 0 28 28" fill="none" stroke="var(--icon-blue)" stroke-width="1.8"><circle cx="14" cy="14" r="11"/><circle cx="14" cy="11.5" r="4"/><path d="M6.5 22c2-3.5 4.5-5 7.5-5s5.5 1.5 7.5 5"/></svg>
        <span class="detail-label">Student Name:</span><span class="detail-value">Leo Marsh</span>
      </li>
      <li class="detail" style="top:156px">
        <svg viewBox="0 0 28 28" fill="none" stroke="var(--icon-blue)" stroke-width="1.6"><rect x="3" y="5" width="20" height="18" rx="2"/><path d="M3 10h20M8 3v4M18 3v4"/><circle cx="21" cy="21" r="4.5" fill="var(--row-bg)"/><path d="M19 21l1.5 1.5 2.5-3"/></svg>
        <span class="detail-label">Appointment:</span><span class="detail-value">School Admission</span>
      </li>
      <li class="detail" style="top:239px">
        <svg viewBox="0 0 28 28" fill="none" stroke="var(--icon-blue)" stroke-width="1.8" stroke-linecap="round"><circle cx="18" cy="5" r="2.5"/><path d="M16 9l-4 6 4 3-2 7M12 15l-5 6M14 10l6 3 3-2M5 11h5"/></svg>
        <span class="detail-label">Service:</span><span class="detail-value">Kids Sports Classes</span>
      </li>
      <li class="detail" style="top:321px">
        <svg viewBox="0 0 28 28" fill="none" stroke="var(--icon-blue)" stroke-width="1.6"><rect x="3" y="5" width="22" height="19" rx="2"/><path d="M3 10h22M8 3v4M20 3v4M7 14h2M12 14h2M17 14h2M7 18h2M12 18h2M17 18h2"/></svg>
        <span class="detail-label">Start Date:</span><span class="detail-value">16.02.2023</span>
      </li>
      <li class="detail" style="top:404px">
        <svg viewBox="0 0 28 28" fill="none" stroke="var(--icon-blue)" stroke-width="1.6"><rect x="3" y="5" width="20" height="18" rx="2"/><path d="M3 10h20M8 3v4M18 3v4M7 14h2M12 14h2M7 18h2"/><circle cx="21" cy="21" r="4.5" fill="var(--row-bg)"/><path d="M19 21l1.5 1.5 2.5-3"/></svg>
        <span class="detail-label">End Date:</span><span class="detail-value">18.04.2026</span>
      </li>
      <li class="detail" style="top:486px">
        <svg viewBox="0 0 28 28" fill="none" stroke="var(--icon-blue)" stroke-width="1.8" stroke-linecap="round"><path d="M11 3h6M14 3v3"/><circle cx="13" cy="15" r="9"/><path d="M13 15V10"/><path d="M19 18l5 3-5 3z" fill="var(--icon-blue)"/></svg>
        <span class="detail-label">Start Time:</span><span class="detail-value">8 am</span>
      </li>
      <li class="detail" style="top:572px">
        <svg viewBox="0 0 28 28" fill="none" stroke="var(--icon-blue)" stroke-width="1.8" stroke-linecap="round"><path d="M3 6l3-3M25 6l-3-3M11 2h6"/><circle cx="13" cy="15" r="9"/><path d="M13 15V10"/><path d="M19 18l5 3-5 3z" fill="var(--icon-blue)"/></svg>
        <span class="detail-label">End Time:</span><span class="detail-value">4 pm</span>
      </li>
    </ul>
  </main>

  <footer>
    <nav class="social" aria-label="Social links">
      <span class="social-link" role="img" aria-label="Social network link"></span>
      <span class="social-link alt" role="img" aria-label="Social network link"></span>
      <span class="social-link deep" role="img" aria-label="Social network link"></span>
    </nav>
    <p class="footer-note">You elected to recieve Notification emails.<br>No longer interested? Unsubscribe or manage your subscriptions.</p>
    <p class="copyright">Copyright© 2023</p>
  </footer>
</body>
</html>
```